integrative health clinic-Medical massage, acupuncture, chiropractic

we like our logo, but are open to new ideas. We need a new card design. We have added chiropractic and acupuncture that we have put under the name of the business. We are an integrative medical clinic

Target Market(s)

General public, athletes

Contact Information for Business Card

Phone 5055582917
Fax 5055582916
Hours Monday-Friday 9-6
Saturday 10-6
The 20% can be smaller on the back

Colors
3176b5
0355a3

Requirements
Must have
• Logo but am open to ideas
Nice to have
• We are an integrated medical clinic but also want to be personable. We want the card fun and inviting

```html
<!DOCTYPE html>
<html lang="en">
<head>
<meta charset="utf-8">
<title>Sage Mesa Wellness – Business Card</title>
<link href="https://fonts.googleapis.com/css2?family=Roboto+Condensed:wght@400&family=Crimson+Text:ital@1&family=Ubuntu:ital,wght@0,500;1,500&display=swap" rel="stylesheet">
<style>
  :root {
    --card-blue: #0a55a8;
    --accent-blue: #3176b5;
    --soft-blue: #9dbde3;
    --white: #ffffff;
    --page: #ffffff;
  }
  html, body {
    margin: 0;
    padding: 0;
    width: 800px;
    height: 1200px;
    overflow: hidden;
    background: var(--page);
  }
  .canvas {
    position: relative;
    width: 800px;
    height: 1200px;
  }
  .card {
    position: absolute;
    left: 80px;
    width: 640px;
    height: 366px;
    background: var(--card-blue);
    overflow: hidden;
    color: var(--white);
    font-family: "Ubuntu", sans-serif;
  }
  .card-front { top: 180px; }
  .card-back { top: 654px; }

  .card-decoration {
    position: absolute;
    inset: 0;
    background:
      radial-gradient(circle at 18% 75%, rgba(49,118,181,0.45) 0, rgba(49,118,181,0) 38%),
      radial-gradient(circle at 88% 10%, rgba(49,118,181,0.45) 0, rgba(49,118,181,0) 30%);
  }
  .card-back .card-decoration {
    background:
      radial-gradient(circle at 70% 40%, rgba(49,118,181,0.45) 0, rgba(49,118,181,0) 40%),
      radial-gradient(circle at 10% 90%, rgba(49,118,181,0.4) 0, rgba(49,118,181,0) 30%);
  }

  .brand-name {
    position: absolute;
    left: 145px;
    top: 74px;
    margin: 0;
    font-family: "Roboto Condensed", sans-serif;
    font-weight: 400;
    font-size: 42px;
    letter-spacing: -0.5px;
    line-height: 1;
  }
  .brand-dot {
    position: absolute;
    left: 172px;
    top: 128px;
    width: 22px;
    height: 22px;
    border-radius: 50%;
    background: var(--white);
  }
  .tagline {
    position: absolute;
    left: 232px;
    top: 122px;
    margin: 0;
    font-family: "Crimson Text", serif;
    font-style: italic;
    font-size: 20px;
    color: #dbe6f4;
  }
  .address {
    position: absolute;
    left: 365px;
    top: 174px;
    margin: 0;
    font-style: italic;
    font-weight: 500;
    font-size: 18px;
    line-height: 24px;
  }
  .contact-line {
    position: absolute;
    left: 58px;
    display: flex;
    align-items: center;
    gap: 10px;
    font-style: italic;
    font-weight: 500;
    font-size: 13px;
  }
  .contact-phone { top: 260px; }
  .contact-fax { top: 306px; }
  .contact-line svg { width: 22px; height: 22px; fill: var(--white); }
  .hours {
    position: absolute;
    left: 403px;
    top: 292px;
    display: flex;
    align-items: center;
    gap: 10px;
    font-style: italic;
    font-weight: 500;
    font-size: 11.5px;
    line-height: 15px;
  }
  .hours svg { width: 22px; height: 22px; }

  .offer-tab {
    position: absolute;
    left: 0;
    top: 24px;
    width: 154px;
    height: 72px;
    background: var(--accent-blue);
    border-top-right-radius: 60px 72px;
  }
  .offer-percent {
    position: absolute;
    left: 44px;
    top: 40px;
    font-style: italic;
    font-weight: 500;
    font-size: 34px;
    color: var(--soft-blue);
    line-height: 1;
  }
  .offer-text {
    position: absolute;
    left: 152px;
    top: 50px;
    font-style: italic;
    font-weight: 500;
    font-size: 24px;
    color: var(--soft-blue);
    letter-spacing: 0.5px;
    line-height: 1;
  }
  .specialties {
    position: absolute;
    left: 0;
    right: 0;
    top: 172px;
    margin: 0;
    text-align: center;
    font-style: italic;
    font-weight: 500;
    font-size: 19px;
  }
  .back-brand {
    position: absolute;
    left: 50px;
    top: 290px;
    display: flex;
    align-items: center;
    gap: 8px;
    font-weight: 500;
    font-size: 15px;
  }
  .back-brand .brand-mark {
    width: 16px;
    height: 16px;
    border-radius: 50%;
    background: var(--white);
  }
  .booking {
    position: absolute;
    left: 232px;
    width: 200px;
    top: 280px;
    text-align: center;
    font-weight: 500;
    font-size: 17px;
    line-height: 26px;
    margin-left: 0;
  }
  .booking-url {
    display: block;
    font-style: italic;
    white-space: nowrap;
    margin-left: -60px;
    margin-right: -60px;
  }
</style>
</head>
<body>
<main class="canvas">

  <section class="card card-front" aria-label="Business card front">
    <div class="card-decoration" role="img" aria-label="Faint swirl decoration in lighter blue"></div>
    <h1 class="brand-name">Sage Mesa Wellness</h1>
    <span class="brand-dot"></span>
    <p class="tagline">Sports Therapy and Wellness Center</p>
    <p class="address">1427 Cerrillos Rd, H2<br>Santa Fe,NM 81507</p>

    <div class="contact-line contact-phone">
      <svg viewBox="0 0 24 24" aria-hidden="true"><path d="M6.6 10.8a15.1 15.1 0 0 0 6.6 6.6l2.2-2.2c.3-.3.7-.4 1-.2 1.1.4 2.3.6 3.6.6.6 0 1 .4 1 1V20c0 .6-.4 1-1 1A17 17 0 0 1 3 4c0-.6.4-1 1-1h3.5c.6 0 1 .4 1 1 0 1.3.2 2.5.6 3.6.1.3 0 .7-.2 1z"/></svg>
      <span>Phone 5055582917</span>
    </div>
    <div class="contact-line contact-fax">
      <svg viewBox="0 0 24 24" aria-hidden="true"><path d="M7 3h10v4H7z"/><path d="M4 8h16a2 2 0 0 1 2 2v6h-4v-3H6v3H2v-6a2 2 0 0 1 2-2z"/><path d="M7 14h10v7H7z"/></svg>
      <span>Fax 5055582916</span>
    </div>
    <div class="hours">
      <svg viewBox="0 0 24 24" aria-hidden="true"><circle cx="12" cy="12" r="9" fill="none" stroke="#fff" stroke-width="2"/><path d="M12 7v5l3 3" fill="none" stroke="#fff" stroke-width="2" stroke-linecap="round"/></svg>
      <span>Monday-Friday 9am-6pm<br>Saturday 10am-6pm</span>
    </div>
  </section>

  <section class="card card-back" aria-label="Business card back">
    <div class="card-decoration" role="img" aria-label="Faint swirl decoration in lighter blue"></div>
    <div class="offer-tab"></div>
    <span class="offer-percent">20%</span>
    <span class="offer-text">OFF FIRST VISIT</span>
    <p class="specialties">Specializing In Medical,sports Massage And Manual Therapies</p>
    <div class="back-brand">
      <span class="brand-mark"></span>
      <span>Sage Mesa Wellness</span>
    </div>
    <p class="booking">BOOK ONLINE<span class="booking-url">www.sagemesawellnessnm.com</span></p>
  </section>

</main>
</body>
</html>
```